Psychiatrist/ Psychotherapist needs a letterhead design

I am a Psychiatrist working in private practice. I work as a psychotherapist and treat patients with depression, anxiety, post traumatic stress and relationship problems. I need a letterhead which is elegant and professional. I would like to see designs using colours such as blues and greys.
I would like the information on the letterhead split between the top and bottom of the page to give it a look of balance.
I want it to look elegant, feminine and upmarket. I don't want it to look too corporate but to show some flair and to be a bit artistic.

Target Market(s)

Other doctors, specialists and agencies who have referred patients to me.

Industry/Entity Type

Work

Font styles to use
Script

Requirements
Must have
• My name and my profession psychiatrist need to be highlighted and prominent. It needs to be professional looking and elegant without being old fashioned or too conservative.
Nice to have
• Balance between the top and bottom of the page.
Should not have
• I don't want fonts which are old and too traditional.

```html
<!DOCTYPE html>
<html lang="en">
<head>
<meta charset="utf-8">
<title>Dr. Claire Ashworth – Psychiatrist Letterhead</title>
<link href="https://fonts.googleapis.com/css2?family=Open+Sans:wght@400;500&family=Tinos&display=swap" rel="stylesheet">
<style>
  :root {
    --slate: #647885;
    --slate-dark: #5a6e7b;
    --mist: #a9a9ae;
    --band-grey: #d9d9d9;
    --ink: #2e2e2e;
    --ink-soft: #3c3c3c;
    --paper: #ffffff;
  }
  html, body {
    margin: 0;
    padding: 0;
    overflow: hidden;
    background: var(--paper);
  }
  .letterhead {
    position: relative;
    width: 850px;
    height: 1200px;
    overflow: hidden;
    background: var(--paper);
    font-family: "Open Sans", Arial, sans-serif;
  }
  .header-band {
    position: absolute;
    left: 0; top: 0;
    width: 850px; height: 250px;
    background: linear-gradient(to bottom, var(--band-grey) 0%, #ececec 45%, var(--paper) 100%);
  }
  .footer-band {
    position: absolute;
    left: 0; bottom: 0;
    width: 850px; height: 240px;
    background: linear-gradient(to top, var(--band-grey) 0%, #e6e6e6 55%, var(--paper) 100%);
  }
  .decor {
    position: absolute;
    left: 0; top: 0;
  }
  .practitioner-name {
    position: absolute;
    left: 112px; top: 60px;
    margin: 0;
    font-size: 29px;
    font-weight: 400;
    color: var(--ink);
    letter-spacing: 0.1px;
    line-height: 1;
  }
  .credentials {
    position: absolute;
    left: 115px; top: 94px;
    margin: 0;
    font-size: 15px;
    color: var(--ink-soft);
    line-height: 1;
  }
  .profession-bar {
    position: absolute;
    left: 401px; top: 62px;
    width: 449px; height: 43px;
    background: var(--slate);
    display: flex;
    align-items: center;
  }
  .profession {
    margin: 0 0 0 14px;
    font-family: "Tinos", "Times New Roman", serif;
    font-size: 31px;
    font-weight: 400;
    color: var(--paper);
    letter-spacing: 13.4px;
    line-height: 1;
    white-space: nowrap;
  }
  .contact-list {
    position: absolute;
    left: 49px; top: 1028px;
    margin: 0; padding: 0;
    list-style: none;
  }
  .contact-item {
    display: flex;
    align-items: center;
    height: 26.5px;
    font-size: 14.5px;
    color: var(--ink);
  }
  .contact-icon {
    width: 12px; height: 12px;
    margin-right: 12px;
    flex: none;
  }
</style>
</head>
<body>
  <main class="letterhead">
    <div class="header-band"></div>
    <div class="footer-band"></div>

    <svg class="decor" width="850" height="1200" viewBox="0 0 850 1200" aria-hidden="true">
      <g class="corner-circles top-left">
        <circle cx="12" cy="24" r="48" fill="var(--slate-dark)"/>
        <circle cx="83" cy="27" r="36" fill="var(--mist)"/>
        <circle cx="36" cy="120" r="58" fill="var(--slate)"/>
      </g>
      <g class="corner-circles bottom-right">
        <circle cx="794" cy="1037" r="57" fill="var(--slate)"/>
        <circle cx="732" cy="1112" r="36" fill="var(--mist)"/>
        <circle cx="823" cy="1160" r="65" fill="var(--slate)"/>
      </g>
    </svg>

    <header>
      <h1 class="practitioner-name">Dr. Claire Ashworth</h1>
      <p class="credentials">B.Med, FRANZCP</p>
      <div class="profession-bar">
        <p class="profession">PSYCHIATRIST</p>
      </div>
    </header>

    <footer>
      <ul class="contact-list">
        <li class="contact-item">
          <svg class="contact-icon" viewBox="0 0 12 12" aria-label="Address">
            <rect width="12" height="12" rx="2" fill="var(--slate)"/>
            <path d="M6 2.4a2.3 2.3 0 0 0-2.3 2.3C3.7 6.5 6 9.6 6 9.6s2.3-3.1 2.3-4.9A2.3 2.3 0 0 0 6 2.4z" fill="var(--paper)"/>
          </svg>
          14 Fenwick Lane, Norwood, SA 5067
        </li>
        <li class="contact-item">
          <svg class="contact-icon" viewBox="0 0 12 12" aria-label="Phone">
            <rect width="12" height="12" rx="2" fill="var(--slate)"/>
            <path d="M2.6 4.4c0-1 1.5-1.5 3.4-1.5s3.4.5 3.4 1.5v.6H7.8v-.7H4.2V5H2.6zM3.6 5.8h4.8l.6 3H3z" fill="var(--paper)"/>
          </svg>
          (08) 8412 6034
        </li>
        <li class="contact-item">
          <svg class="contact-icon" viewBox="0 0 12 12" aria-label="Fax">
            <rect width="12" height="12" rx="2" fill="var(--slate)"/>
            <rect x="2.5" y="3" width="7" height="6" fill="none" stroke="var(--paper)" stroke-width="1"/>
            <line x1="2.5" y1="5" x2="9.5" y2="5" stroke="var(--paper)" stroke-width="1"/>
          </svg>
          (08) 8412 6035
        </li>
        <li class="contact-item">
          <svg class="contact-icon" viewBox="0 0 12 12" aria-label="Mobile">
            <rect width="12" height="12" rx="2" fill="var(--slate)"/>
            <rect x="4" y="2" width="4" height="8" rx="0.8" fill="var(--paper)"/>
          </svg>
          0412558771
        </li>
        <li class="contact-item">
          <svg class="contact-icon" viewBox="0 0 12 12" aria-label="Email">
            <rect width="12" height="12" rx="2" fill="var(--slate)"/>
            <rect x="2.5" y="3.5" width="7" height="5" fill="none" stroke="var(--paper)" stroke-width="1"/>
            <path d="M2.5 3.5L6 6.4l3.5-2.9" fill="none" stroke="var(--paper)" stroke-width="1"/>
          </svg>
          cashworth@mindcare.net.au
        </li>
      </ul>
    </footer>
  </main>
</body>
</html>
```